Design few pages for professional development app

I need a website design for a prototype project. The goal of the project is to prototype a few basic screens for a professional development application.

The final design should be clean, modern, and appeal to a professional millenial clientele.The designs have been wireframed (see attached), and we'd like these wireframes converted to design files.

Here is the list of goals and tasks that correspond to the design: https://files.plumvarko.net/sheets/d/8qHvR03kxTwe1mZpLa56NuYcdoQ42BsJfEi7gKt0XyWn/edit?usp=sharing

Number of Pages Required

5+ page

Font styles to use
Serif
Sans Serif

Colors

Designer to choose colors to be used in the design.

Requirements
Nice to have
• Uses Google Material Design, Bootstrap, or another framework

```html
<!DOCTYPE html>
<html lang="en">
<head>
<meta charset="utf-8">
<title>Summitly – Professional Development App Screens</title>
<link href="https://fonts.googleapis.com/css2?family=Roboto:wght@300;400;500;700&display=swap" rel="stylesheet">
<style>
:root{
  --bg:#1b1c1e;
  --bg-shape:#2b2c2f;
  --bg-shape-2:#35363a;
  --blue:#2f7cf6;
  --blue-dark:#1f5fd0;
  --ink:#2b2f36;
  --muted:#7b818b;
  --line:#d9dde3;
  --panel:#ffffff;
  --soft:#f3f5f8;
  --gold:#f2b632;
}
*{box-sizing:border-box;margin:0;padding:0}
html,body{width:1200px;height:3208px;overflow:hidden}
body{background:var(--bg);font-family:"Roboto",Arial,sans-serif;color:var(--ink);position:relative}
.backdrop{position:absolute;inset:0;width:1200px;height:3208px}
.brand-top{position:absolute;top:56px;left:0;width:1200px;display:flex;justify-content:center;align-items:center;gap:14px}
.brand-top .dot{width:26px;height:26px;border-radius:50%;background:var(--blue)}
.brand-top .name{font-size:44px;font-weight:500;color:#fff}
.screen-label{position:absolute;left:0;width:1200px;text-align:center;color:var(--blue);font-size:28px;font-weight:400}
.screen{position:absolute;left:112px;width:976px;background:var(--panel);overflow:hidden;box-shadow:0 10px 30px rgba(0,0,0,.35)}
.app-bar{height:56px;display:flex;align-items:center;justify-content:space-between;padding:0 28px;border-bottom:1px solid #eceef2}
.app-brand{display:flex;align-items:center;gap:8px;font-size:20px;font-weight:500;color:var(--blue)}
.app-brand .dot{width:12px;height:12px;border-radius:50%;background:var(--blue)}
.search{width:18px;height:18px}
.btn{display:inline-flex;align-items:center;justify-content:center;gap:8px;border-radius:4px;font-size:12px;font-weight:500;letter-spacing:.8px;text-transform:uppercase;white-space:nowrap}
.btn-primary{background:var(--blue);color:#fff}
.btn-outline{border:1px solid var(--blue);color:var(--blue);background:#fff}
.btn-text{color:var(--blue)}
.accent{color:var(--blue)}

/* Screen 1 */
.hero{position:absolute;top:56px;left:0;right:0;height:300px}
.hero-title{position:absolute;left:44px;top:50px;font-size:40px;font-weight:300;color:var(--ink);white-space:nowrap}
.hero-title strong{font-weight:500;color:var(--blue)}
.hero-sub{position:absolute;left:44px;top:112px;width:400px;font-size:15px;line-height:1.45;color:#4a505a}
.hero-ready{position:absolute;left:44px;top:176px;font-size:13px;font-weight:500}
.hero-hint{position:absolute;left:44px;top:196px;font-size:11px;color:var(--muted)}
.hero .btn{position:absolute;left:44px;top:226px;width:150px;height:36px}
.hero-art{position:absolute;left:560px;top:18px;width:380px;height:270px;border-radius:6px;background:linear-gradient(135deg,#eaf2ff 0%,#9cc2ff 45%,#2f7cf6 75%,#f2b632 100%)}
.testimonials{position:absolute;left:44px;right:44px;top:378px;height:170px;background:var(--soft);display:flex;align-items:flex-start;padding:28px 30px}
.quote-mark{font-size:72px;line-height:.8;color:var(--blue);font-weight:700;margin-right:10px;width:40px}
.testimonial{display:flex;gap:16px;align-items:flex-start;width:400px;padding-top:40px}
.avatar{width:56px;height:56px;border-radius:50%;flex:none;background:linear-gradient(135deg,#d8c2a8,#8a6a52)}
.avatar.two{background:linear-gradient(135deg,#b8b0a6,#4f4640)}
.testimonial p{font-size:13px;line-height:1.45;color:#4a505a}
.testimonial .who{display:block;margin-top:8px;font-size:11px;color:var(--blue)}

/* Form cards */
.card{position:absolute;left:218px;width:540px;background:#fff;border-radius:4px;box-shadow:0 2px 14px rgba(0,0,0,.16);padding:30px 56px}
.card h2{font-size:30px;font-weight:300;text-align:center;color:var(--ink);white-space:nowrap}
.card h2 strong{font-weight:500;color:var(--blue)}
.field{margin-top:18px}
.field label{display:block;font-size:11px;color:var(--muted);margin-bottom:6px}
.field .input{height:30px;border:1px solid var(--line);border-radius:3px;font-size:13px;padding:6px 10px}
.field.active label{color:var(--blue)}
.field.active .input{border-color:var(--blue);background:#eef4ff}
.field.short .input{width:190px}
.agree{display:flex;align-items:center;gap:6px;margin-top:20px;font-size:11px;color:var(--muted)}
.box{width:14px;height:14px;border:1px solid #a9afb8;border-radius:2px;flex:none}
.form-actions{display:flex;justify-content:center;gap:20px;margin-top:24px}
.form-actions .btn{height:32px;padding:0 22px}

/* Screen 3 */
.card p.lead{text-align:center;font-size:15px;color:#4a505a;margin-top:10px}
.goals{margin:28px auto 0;width:300px;display:flex;flex-direction:column;gap:14px}
.goal{height:46px;display:flex;align-items:center;gap:14px;padding:0 16px;border-radius:3px;background:#fff;box-shadow:0 1px 5px rgba(0,0,0,.14);font-size:13px}
.goal .icon{width:26px;height:26px;border-radius:50%;flex:none;background:linear-gradient(135deg,#f2b632,#2f7cf6)}
.goal.selected{background:var(--blue);color:#fff}
.goal.selected .box{background:#fff;border-color:#fff;display:flex;align-items:center;justify-content:center}
.goal.selected .icon{background:linear-gradient(135deg,#ffffff,#9cc2ff)}
.see-list{display:block;text-align:center;font-size:12px;color:var(--blue);margin-top:34px}

/* Screen 4 */
.tasks-title{position:absolute;left:44px;top:84px;font-size:28px;font-weight:400}
.tasks-title strong{font-weight:500;color:var(--blue)}
.task-grid{position:absolute;left:44px;top:150px;width:888px;display:grid;grid-template-columns:repeat(3,1fr);gap:52px 24px}
.task{height:180px;background:#fff;box-shadow:0 1px 8px rgba(0,0,0,.14);border-radius:3px;padding:20px 20px}
.task h3{font-size:16px;font-weight:400;color:var(--blue)}
.task p{font-size:13px;color:#4a505a;margin-top:22px}
.task .btn{margin-top:22px;width:100%;height:30px}
</style>
</head>
<body>

<svg class="backdrop" viewBox="0 0 1200 3208" aria-hidden="true">
  <polygon points="0,250 330,250 80,1100 0,1100" fill="var(--bg-shape)"/>
  <polygon points="0,170 140,170 0,640" fill="var(--blue-dark)" opacity=".8"/>
  <polygon points="620,1180 1200,1180 1200,1500 780,1500" fill="var(--bg-shape)"/>
  <polygon points="900,860 1200,860 1200,1700" fill="var(--blue)" opacity=".85"/>
  <polygon points="960,1500 1200,1500 1200,2400 1100,2400" fill="var(--bg-shape-2)"/>
  <polygon points="0,1900 260,1900 0,2700" fill="var(--bg-shape)"/>
  <polygon points="760,2560 1200,2320 1200,3208 620,3208" fill="var(--bg-shape)"/>
</svg>

<div class="brand-top"><span class="dot"></span><span class="name">Summitly</span></div>

<!-- Screen 1 -->
<div class="screen-label" style="top:280px">Screen 1</div>
<section class="screen" style="top:352px;height:576px">
  <div class="app-bar">
    <div class="app-brand"><span class="dot"></span>Summitly</div>
    <svg class="search" viewBox="0 0 24 24"><circle cx="10" cy="10" r="6" fill="none" stroke="#555" stroke-width="2"/><line x1="15" y1="15" x2="21" y2="21" stroke="#555" stroke-width="2"/></svg>
  </div>
  <div class="hero">
    <h1 class="hero-title">Take control of <strong>your Career</strong></h1>
    <p class="hero-sub">Complete short, actionable tasks guaranteed to get you further in your career, faster than ever</p>
    <p class="hero-ready">Ready to get started?</p>
    <p class="hero-hint">Take the short quiz below and get your personalised path today.</p>
    <span class="btn btn-primary">Get started
      <svg width="14" height="10" viewBox="0 0 14 10"><path d="M0 5h12M8 1l4 4-4 4" fill="none" stroke="#fff" stroke-width="1.6"/></svg>
    </span>
    <div class="hero-art" role="img" aria-label="Illustration of people climbing rising bar charts toward a target"></div>
  </div>
  <div class="testimonials">
    <div class="quote-mark">“</div>
    <div class="testimonial">
      <div class="avatar" role="img" aria-label="Portrait of a smiling customer"></div>
      <p>I love how quickly I can do the tasks, and see the progress.<span class="who">Mary Lane</span></p>
    </div>
    <div class="testimonial">
      <div class="avatar two" role="img" aria-label="Portrait of a customer"></div>
      <p>The best investment I've made in myself in ages.<span class="who">Ben Carter</span></p>
    </div>
  </div>
</section>

<!-- Screen 2 -->
<div class="screen-label" style="top:960px">Screen 2</div>
<section class="screen" style="top:1032px;height:568px">
  <div class="app-bar">
    <div class="app-brand"><span class="dot"></span>Summitly</div>
    <svg class="search" viewBox="0 0 24 24"><circle cx="10" cy="10" r="6" fill="none" stroke="#555" stroke-width="2"/><line x1="15" y1="15" x2="21" y2="21" stroke="#555" stroke-width="2"/></svg>
  </div>
  <form class="card" style="top:84px">
    <h2>Sign up to see &amp; Save your <strong>Goals</strong></h2>
    <div class="field active"><label>Name*</label><div class="input">John Doe</div></div>
    <div class="field"><label>Email*</label><div class="input"></div></div>
    <div class="field short"><label>Password*</label><div class="input"></div></div>
    <div class="field short"><label>Re-type password*</label><div class="input"></div></div>
    <div class="agree"><span class="box"></span>I agree to the <span class="accent">Terms of Use</span> and <span class="accent">Privacy Policy</span></div>
    <div class="form-actions"><span class="btn btn-primary">Sign up</span><span class="btn btn-text">Login instead</span></div>
  </form>
</section>

<!-- Screen 3 -->
<div class="screen-label" style="top:1640px">Screen 3</div>
<section class="screen" style="top:1712px;height:608px">
  <div class="app-bar">
    <div class="app-brand"><span class="dot"></span>Summitly</div>
    <svg class="search" viewBox="0 0 24 24"><circle cx="10" cy="10" r="6" fill="none" stroke="#555" stroke-width="2"/><line x1="15" y1="15" x2="21" y2="21" stroke="#555" stroke-width="2"/></svg>
  </div>
  <div class="card" style="top:100px;height:460px">
    <h2>What are your <strong>Main Goals?</strong></h2>
    <p class="lead">Tell us what you would like to achieve with Summitly</p>
    <div class="goals">
      <div class="goal selected"><span class="box"><svg width="10" height="8" viewBox="0 0 10 8"><path d="M1 4l3 3 5-6" fill="none" stroke="#2f7cf6" stroke-width="1.8"/></svg></span><span class="icon" role="img" aria-label="Network icon"></span>Build my Network</div>
      <div class="goal"><span class="box"></span><span class="icon" role="img" aria-label="Star icon"></span>Personal Branding</div>
      <div class="goal"><span class="box"></span><span class="icon" role="img" aria-label="Rocket icon"></span>Get a promotion</div>
      <div class="goal"><span class="box"></span><span class="icon" role="img" aria-label="Flag icon"></span>Be a Better leader</div>
    </div>
    <span class="see-list">See my personalized List</span>
  </div>
</section>

<!-- Screen 4 -->
<div class="screen-label" style="top:2360px">Screen 4</div>
<section class="screen" style="top:2424px;height:736px">
  <div class="app-bar">
    <div class="app-brand"><span class="dot"></span>Summitly</div>
    <svg class="search" viewBox="0 0 24 24"><circle cx="10" cy="10" r="6" fill="none" stroke="#555" stroke-width="2"/><line x1="15" y1="15" x2="21" y2="21" stroke="#555" stroke-width="2"/></svg>
  </div>
  <h2 class="tasks-title"><strong>Mary</strong>, here's your list of suggested tasks</h2>
  <div class="task-grid">
    <div class="task"><h3>Personal Branding</h3><p>Write your personal brand statement</p><span class="btn btn-primary">✓ Completed</span></div>
    <div class="task"><h3>Get a Promotion</h3><p>Write your personal brand statement</p><span class="btn btn-outline">▶ Start task</span></div>
    <div class="task"><h3>Personal Branding</h3><p>Write your personal brand statement</p><span class="btn btn-outline">▶ Start task</span></div>
    <div class="task"><h3>Personal Branding</h3><p>Write your personal brand statement</p><span class="btn btn-primary">✓ Completed</span></div>
    <div class="task"><h3>Personal Branding</h3><p>Write your personal brand statement</p><span class="btn btn-primary">✓ Completed</span></div>
    <div class="task"><h3>Personal Branding</h3><p>Write your personal brand statement</p><span class="btn btn-primary">✓ Completed</span></div>
  </div>
</section>

</body>
</html>
```